Stationery Design Project

Minimal Design. Black and White Colours Only.
Need Business Card
With Compliments slip
Letterhead
A4 Folder

Target Market(s)

Luxury architectual designed home owners

Industry/Entity Type

Business

Requirements
Must have
• Black and White colours only. Suggest some good textured stock for business card for future printing. try to use font that is used in my logo our some other minimal modern font.

```html
<!DOCTYPE html>
<html lang="en">
<head>
<meta charset="utf-8">
<title>Vale Estates – Business Card</title>
<link rel="stylesheet" href="https://fonts.googleapis.com/css2?family=Questrial&display=swap">
<style>
  :root {
    --backdrop: #e4e1df;
    --card: #ffffff;
    --ink: #111111;
    --edge: #d2cfcc;
  }
  html, body {
    margin: 0;
    width: 1200px;
    height: 1000px;
    overflow: hidden;
    background: var(--backdrop);
    font-family: "Questrial", "Helvetica Neue", Arial, sans-serif;
    color: var(--ink);
  }
  .business-card {
    position: absolute;
    left: 242px;
    top: 274px;
    width: 716px;
    height: 438px;
    background: var(--card);
    border: 1px solid var(--edge);
    box-sizing: border-box;
  }
  .brand {
    position: absolute;
    left: 126px;
    top: 130px;
    display: flex;
    align-items: center;
    gap: 40px;
  }
  .brand-mark {
    width: 70px;
    height: 70px;
    background: var(--ink);
  }
  .brand-name {
    font-size: 40px;
    letter-spacing: 0.5px;
    line-height: 1;
    margin-top: 6px;
  }
  .person-name {
    position: absolute;
    left: 245px;
    top: 208px;
    font-size: 33px;
    line-height: 1;
    margin: 0;
    font-weight: 400;
  }
  .person-title {
    position: absolute;
    left: 245px;
    top: 251px;
    font-size: 21px;
    line-height: 1;
    letter-spacing: 0.3px;
  }
  .rule {
    position: absolute;
    top: 262px;
    height: 2px;
    background: var(--ink);
  }
  .rule-left { left: 14px; width: 216px; }
  .rule-right { left: 482px; width: 218px; }
  .address, .contact {
    position: absolute;
    top: 376px;
    font-size: 14px;
    line-height: 17px;
    text-align: center;
  }
  .address { left: 6px; width: 180px; }
  .contact { right: 12px; width: 220px; }
  .contact span { display: block; }
</style>
</head>
<body>
  <section class="business-card">
    <div class="brand">
      <div class="brand-mark"></div>
      <div class="brand-name">VALE ESTATES</div>
    </div>
    <h1 class="person-name">Daniel Hartley</h1>
    <div class="person-title">Managing Director</div>
    <div class="rule rule-left"></div>
    <div class="rule rule-right"></div>
    <address class="address" style="font-style:normal">
      Level 12, 48 Harbour Rd<br>
      Carlton QLD 4100<br>
      Australia
    </address>
    <div class="contact">
      <span>M: +61 400 555 012</span>
      <span>P: +61 7 5550 0147</span>
      <span>E: dhartley@valeestates.com</span>
    </div>
  </section>
</body>
</html>
```